Forge Youth Now Website Re-design

The goal of this website redesign is to give Forge Youth Now, a nonprofit focused on recruiting conservative candidates for public office to state and local positions, a platform that balances youthful energy with a sense of maturity and credibility. This site should not only inspire young conservatives across the country to get involved but also position the organization as a leader in cultivating the next generation of public servants. A clean, professional layout will convey trustworthiness, while bold visuals, clean animations, and design motifs will reinforce the patriotic and dynamic nature of the brand. Central to this design is an interactive or static map showcasing our Bright Torches from across the nation as the main home page, helping users quickly understand the breadth of the movement. See design brief for more.

Target Market(s)

18-35 year old American political conservatives

Coding

Coded - Design and coding required

Number of Pages Required

5+ page

Font styles to use
Sans Serif

Requirements
Nice to have
• An active or Static map that is representative of our membership. We will provide data but an example will do

```html
<!DOCTYPE html>
<html lang="en">
<head>
<meta charset="utf-8">
<title>Forge Youth Now</title>
<link rel="stylesheet" href="https://fonts.googleapis.com/css2?family=Bebas+Neue&family=Montserrat:wght@400;500;600;700&display=swap">
<style>
:root{
  --navy:#1c2c68;
  --navy-deep:#15224f;
  --red:#c61f2e;
  --red-deep:#a8182a;
  --ink:#1e2a55;
  --grey:#eef0f4;
  --white:#ffffff;
  --black:#111111;
}
*{box-sizing:border-box;margin:0;padding:0}
html,body{width:1200px;height:4628px;overflow:hidden;background:var(--white)}
body{position:relative;font-family:"Montserrat",sans-serif;color:var(--ink)}
.abs{position:absolute}
.display{font-family:"Bebas Neue",sans-serif;font-weight:400;letter-spacing:.5px;line-height:.95}
.photo{position:absolute;overflow:hidden}

/* header */
.site-header{left:0;top:0;width:1200px;height:112px;background:var(--white)}
.brand{left:44px;top:30px;font-family:"Bebas Neue",sans-serif;font-size:40px;color:var(--navy);display:flex;align-items:center;gap:10px}
.brand .dot{width:16px;height:16px;background:var(--red)}
.donate-top{right:52px;top:22px;font-size:14px;font-weight:700;color:var(--navy);display:flex;gap:8px;align-items:center}
.donate-top span.box{width:12px;height:12px;background:var(--red);display:inline-block}
.nav{left:318px;top:72px;display:flex;gap:0;font-size:14px;font-weight:600;color:var(--navy);text-transform:uppercase}
.nav a{display:block;padding:8px 26px;color:inherit;text-decoration:none}
.nav a.active{border-bottom:3px solid var(--red);color:var(--navy)}

/* hero */
.hero{left:0;top:112px;width:1200px;height:548px;background:linear-gradient(100deg,#203a7a 0%,#38609c 45%,#8fb0d6 70%,#c9d6e6 100%)}
.hero-title{left:92px;top:170px;width:560px;font-size:60px;color:var(--white)}
.hero-copy{left:92px;top:420px;width:520px;font-size:16px;line-height:1.45;color:var(--white)}
.btn{display:inline-block;background:var(--red);color:var(--white);font-family:"Bebas Neue",sans-serif;font-size:24px;padding:12px 34px;border-radius:30px}
.hero .btn{position:absolute;left:92px;top:455px}

/* it's time */
.time{left:0;top:660px;width:1200px;height:720px;background:var(--white)}
.time-shade{left:760px;top:660px;width:440px;height:420px;background:linear-gradient(160deg,#e9ebf0,#ffffff)}
.time-accent{left:84px;top:1120px;width:260px;height:180px;background:var(--red);border-radius:0 0 0 40px}
.time-photo{left:100px;top:800px;width:500px;height:490px;border-radius:40px 0 40px 0;background:linear-gradient(170deg,#d9e4ef 0%,#b33a44 55%,#3a4f86 100%)}
.time-title{left:664px;top:888px;font-size:90px;color:var(--red)}
.time-copy{left:664px;top:985px;width:480px;font-size:24px;line-height:1.3;color:var(--navy)}

/* quote band */
.quote{left:0;top:1392px;width:1200px;height:648px;background:var(--navy)}
.quote-text{left:92px;top:1468px;width:490px;font-size:21px;line-height:1.42;color:var(--white)}
.quote-name{left:92px;top:1850px;width:420px;font-size:48px;color:var(--white)}
.quote-rule{left:92px;top:1840px;width:8px;height:92px;background:var(--red)}
.quote-photo{left:600px;top:1460px;width:512px;height:502px;border-radius:40px;background:linear-gradient(160deg,#6b4a3a 0%,#8a2a30 45%,#c82a38 100%)}
.quote-mark{left:540px;top:1748px;width:140px;height:132px;background:var(--red);border-radius:0 0 0 30px;display:flex;align-items:center;justify-content:center}

/* become a leader */
.section-title{left:0;top:2090px;width:1200px;text-align:center;font-size:80px;color:var(--navy)}
.section-rule{left:378px;top:2176px;width:444px;height:6px;background:var(--red)}
.leader-photo{left:72px;top:2264px;width:500px;height:496px;border-radius:0 40px 0 40px;background:linear-gradient(180deg,#6aa0d8 0%,#b7d0ea 55%,#e4e2dc 100%)}
.leader-title{left:620px;top:2310px;width:460px;font-size:60px;color:var(--navy)}
.leader-copy{left:620px;top:2450px;width:500px;font-size:22px;line-height:1.35;color:var(--navy)}
.cta-link{font-family:"Bebas Neue",sans-serif;font-size:44px;color:var(--red)}
.leader-cta{left:620px;top:2652px}

/* donate */
.donate-shade{left:0;top:2900px;width:560px;height:480px;background:linear-gradient(180deg,#ffffff 0%,#e3e6ec 100%)}
.donate-title{left:100px;top:2864px;font-size:64px;color:var(--navy)}
.donate-copy{left:100px;top:2938px;width:480px;font-size:22px;line-height:1.38;color:var(--navy)}
.donate-cta{left:100px;top:3200px}
.donate-photo{left:620px;top:2848px;width:500px;height:494px;border-radius:40px 0 40px 0;background:linear-gradient(150deg,#f4e2b8 0%,#b7a38a 45%,#4b4d55 100%)}

/* testimonials */
.testimonials{left:0;top:3424px;width:1200px;height:800px;background:var(--red)}
.testimonials .fade{left:700px;top:3424px;width:500px;height:800px;background:linear-gradient(270deg,var(--red-deep),rgba(168,24,42,0))}
.card{position:absolute;background:var(--white);border-radius:46px;padding:42px 56px;font-size:17px;line-height:1.5;color:#333}
.card-one{left:300px;top:3464px;width:800px;height:250px;border-radius:0 46px 46px 46px;padding-left:96px}
.card-two{left:90px;top:3764px;width:790px;height:246px;border-radius:46px 46px 0 46px}
.avatar{position:absolute;border-radius:50%;border:6px solid var(--white)}
.avatar-one{left:100px;top:3606px;width:200px;height:200px;background:radial-gradient(circle at 50% 40%,#c9a88f,#6b4b3d)}
.avatar-two{left:920px;top:3920px;width:200px;height:200px;background:radial-gradient(circle at 50% 40%,#7a5a48,#2d2b3a)}

/* footer */
.footer{left:0;top:4224px;width:1200px;height:368px;background:linear-gradient(180deg,#f3f4f7,#ffffff)}
.footer-brand{left:40px;top:4290px;font-family:"Bebas Neue",sans-serif;font-size:38px;color:var(--navy);display:flex;align-items:center;gap:10px}
.footer-brand .dot{width:14px;height:14px;background:var(--red)}
.footer-about{left:40px;top:4372px;width:240px;font-size:12px;line-height:1.5;color:#444}
.footer-col{top:4290px;font-size:13px;line-height:2.4;color:#333;list-style:none}
.footer-col li{display:flex;align-items:center;gap:10px}
.footer-col li::before{content:"";width:6px;height:6px;background:var(--red);border-radius:50%}
.col-a{left:340px}
.col-b{left:580px}
.contact{left:880px;top:4290px;width:280px;font-size:13px;line-height:1.6;color:#333}
.contact .row{display:flex;gap:10px;align-items:flex-start;margin-bottom:14px}
.socials{display:flex;gap:10px;margin-top:4px}
.socials span{width:28px;height:28px;border-radius:50%;background:#2b67d6;display:block}
.copyright{left:0;top:4592px;width:1200px;height:36px;background:var(--black);color:#cfcfcf;font-size:12px;text-align:center;line-height:36px}
</style>
</head>
<body>

<header class="abs site-header">
  <div class="abs brand"><span class="dot"></span>Forge Youth Now</div>
  <div class="abs donate-top">DONATE <span class="box"></span></div>
  <nav class="abs nav">
    <a class="active">Home</a><a>About</a><a>Why</a><a>Leadership</a><a>Bright Torches</a><a>Press</a><a>Contact</a>
  </nav>
</header>

<section class="abs hero" role="img" aria-label="Capitol dome under a blue sky framed by blossoming trees"></section>
<h1 class="abs display hero-title">Empowering, Recruiting, &amp; Mentoring the Next Generation of Conservative Leaders</h1>
<p class="abs hero-copy" style="top:420px">Our mission is to prepare Generation Z leaders to take action, take charge, and take control of the future by supporting the vision of the founders of this country. We help them promote conservative political values such as limited government, free market capitalism, individual responsibility, and fiscal restraint.</p>
<a class="abs btn" style="left:92px;top:572px">Get Connected</a>

<section class="abs time"></section>
<div class="abs time-shade"></div>
<div class="abs time-accent"></div>
<div class="photo time-photo" role="img" aria-label="Young woman holding an American flag over her shoulders"></div>
<h2 class="abs display time-title">It's Time.</h2>
<p class="abs time-copy">Our mission is to empower and mentor conservative trailblazers from Generation Z to pursue leadership opportunities, including public office that allow them to work toward a more constitutionally-focused government.</p>

<section class="abs quote"></section>
<p class="abs quote-text">The country's future depends on our ability to help young conservative leaders get engaged, run for office, and make a difference! Forge Youth Now is a powerful tool toward that objective by recruiting and mentoring the next generation of leaders in Iowa and across the nation. I am excited about this opportunity to empower tomorrow's leaders as they help forge America's future."</p>
<div class="abs quote-rule"></div>
<p class="abs display quote-name">Dana Whitfield,<br>Governor of Iowa</p>
<div class="photo quote-photo" role="img" aria-label="Portrait of the governor seated in a red leather chair beside flags"></div>
<div class="abs quote-mark">
  <svg width="70" height="60" viewBox="0 0 70 60" aria-hidden="true"><path d="M4 32h22v28H4zM4 32C4 14 12 4 26 2v10c-8 2-10 10-10 20z" fill="#fff"/><path d="M40 32h22v28H40zM40 32C40 14 48 4 62 2v10c-8 2-10 10-10 20z" fill="#fff"/></svg>
</div>

<h2 class="abs display section-title">Become a Leader</h2>
<div class="abs section-rule"></div>
<div class="photo leader-photo" role="img" aria-label="Capitol dome with an American flag waving in front"></div>
<h3 class="abs display leader-title">The Future Starts<br>With You</h3>
<p class="abs leader-copy">America is shaped by those who protect it and Forge Youth Now is here to support the freedom fighters of tomorrow. Public service is closer than you think, especially with Forge Youth Now on your side.</p>
<a class="abs cta-link leader-cta">Apply Now</a>

<div class="abs donate-shade"></div>
<h3 class="abs display donate-title">Donate Today</h3>
<p class="abs donate-copy">Help fuel the future of the conservative movement right here, right now. Support Forge Youth Now's mission of helping future conservative leaders take office and create change in their communities. Donations of every size helps move this country forward in the right direction.</p>
<a class="abs cta-link donate-cta">Click to Donate</a>
<div class="photo donate-photo" role="img" aria-label="Group of hands holding smartphones together in warm light"></div>

<section class="abs testimonials"></section>
<div class="abs fade"></div>
<div class="card card-one">Lorem ipsum dolor sit amet, consectetur adipiscing elit, sed do eiusmod tempor incididunt ut labore et dolore magna aliqua. Ut enim ad minim veniam, quis nostrud exercitation ullamco laboris nisi ut aliquip ex ea commodo consequat. Duis aute irure dolor in reprehenderit in voluptate velit esse cillum dolore eu fugiat nulla pariatur. Excepteur sint occaecat cupidatat non proident, sunt in culpa qui officia deserunt mollit anim id est laborum.</div>
<div class="avatar avatar-one" role="img" aria-label="Portrait of a smiling young woman"></div>
<div class="card card-two">Lorem ipsum dolor sit amet, consectetur adipiscing elit, sed do eiusmod tempor incididunt ut labore et dolore magna aliqua. Ut enim ad minim veniam, quis nostrud exercitation ullamco laboris nisi ut aliquip ex ea commodo consequat. Duis aute irure dolor in reprehenderit in voluptate velit esse cillum dolore eu fugiat nulla pariatur. Excepteur sint occaecat cupidatat non proident, sunt in culpa qui officia deserunt mollit anim id est laborum.</div>
<div class="avatar avatar-two" role="img" aria-label="Portrait of a smiling man in glasses"></div>

<footer class="abs footer"></footer>
<div class="abs footer-brand"><span class="dot"></span>Forge Youth Now</div>
<p class="abs footer-about">We train young conservatives to run, lead and serve in their towns and states, and we walk with them from first idea to the day they take office.</p>
<ul class="abs footer-col col-a">
  <li>About Us</li><li>Bright Torches</li><li>Become a Buyer</li><li>Become a Seller</li><li>News</li><li>Contact Us</li>
</ul>
<ul class="abs footer-col col-b">
  <li>Batteries &amp; Components</li><li>Batteries &amp; Electricals - Others</li><li>Electric Motor</li><li>Harness &amp; Installation</li><li>Sensors &amp; Actuations</li><li>Sensors &amp; Actuations</li>
</ul>
<div class="abs contact">
  <div class="row">
    <svg width="16" height="20" viewBox="0 0 16 20" aria-hidden="true"><path d="M8 0a7 7 0 0 0-7 7c0 5 7 13 7 13s7-8 7-13a7 7 0 0 0-7-7z" fill="#1c2c68"/><circle cx="8" cy="7" r="2.5" fill="#fff"/></svg>
    <span>Lorem ipsum is simply dummy text of the print</span>
  </div>
  <div class="row">
    <svg width="16" height="16" viewBox="0 0 16 16" aria-hidden="true"><path d="M3 1l3 3-2 2c1 2 3 4 6 6l2-2 3 3-2 2C7 15 1 9 1 3z" fill="#1c2c68"/></svg>
    <span>(515) 555-0148</span>
  </div>
  <div class="row">
    <svg width="16" height="14" viewBox="0 0 16 14" aria-hidden="true"><rect x="1" y="1" width="14" height="12" rx="1" fill="none" stroke="#1c2c68" stroke-width="1.6"/><path d="M1 2l7 6 7-6" fill="none" stroke="#1c2c68" stroke-width="1.6"/></svg>
    <span>hello@forgeyouthnow.org</span>
  </div>
  <div class="socials"><span></span><span></span><span></span></div>
</div>
<div class="abs copyright">Copyright © 2020 forgeyouthnow.org. All rights reserved.</div>

</body>
</html>
```